Bref créative |
Sleek & Easy to navigate web design for a dermatology skin care clinic | ||
Medical practice provides clinical and cosmetic skin care | ||
Medical | ||
skinharborcare.com | ||
New medical practice with multiple locations will provide dermatology skin care services to patients. | ||
We want a website design which will stand out. Please look up other dermatology websites and come up with a design which stands out against the competition. - one idea we thought about was having skin care related photographs which move across the screen |
Cutting-Edge Unique/Creative Professional Friendly Family Oriented Sophisticated Modern Colorful Soft Elegant Nature Progressive Feminine |
left side | ||
The designers are welcome to have a broad range with reference to design concepts for this project. | ||

```html
<!DOCTYPE html>
<html lang="en">
<head>
<meta charset="utf-8">
<title>Skin Harbor Care</title>
<link rel="stylesheet" href="https://fonts.googleapis.com/css2?family=Crimson+Text:ital,wght@0,400;0,600;1,700&family=Arimo:wght@400;700&display=swap">
<style>
:root{
  --green:#4f9a1f;
  --green-dark:#3a7a12;
  --green-light:#a9d36b;
  --ink:#2b2b2b;
  --muted:#5a5a5a;
  --purple:#6e2f5d;
  --page:#ffffff;
  --canvas:#f1f1f1;
  --hero-a:#eef4e4;
  --hero-b:#c9ddb0;
}
*{margin:0;padding:0;box-sizing:border-box}
html,body{width:1200px;height:852px;overflow:hidden}
body{background:var(--canvas);font-family:"Arimo",Arial,sans-serif;color:var(--ink);position:relative}
.page{position:absolute;left:139px;top:0;width:922px;height:852px;background:var(--page);box-shadow:0 0 18px rgba(0,0,0,.12);overflow:hidden}
.brand{position:absolute;left:10px;top:74px;display:flex;align-items:center;gap:8px}
.brand-dot{width:18px;height:18px;border-radius:50%;background:var(--green)}
.brand-name{font-family:"Crimson Text",Georgia,serif;font-weight:600;font-size:21px;color:var(--green-dark);letter-spacing:.5px;text-transform:uppercase;white-space:nowrap}
.phone{position:absolute;right:28px;top:12px;display:flex;align-items:center;gap:10px;font-size:22px;color:var(--ink);white-space:nowrap}
.phone svg{width:22px;height:22px}
.nav{position:absolute;left:372px;top:70px;display:flex;height:30px;align-items:stretch;font-size:14px}
.nav a{color:var(--ink);text-decoration:none;padding:0 15px;display:flex;align-items:center;white-space:nowrap}
.nav a.active{background:var(--green);color:#fff;padding:0 17px}
.nav-rule{position:absolute;left:0;top:100px;width:922px;height:3px;background:var(--green)}
.hero{position:absolute;left:0;top:106px;width:922px;height:426px;background:radial-gradient(ellipse at 30% 50%,#f6e7dc 0%,var(--hero-a) 35%,var(--hero-b) 100%)}
.hero-photo{position:absolute;inset:0}
.arrow{position:absolute;top:183px;width:34px;height:38px;background:rgba(255,255,255,.55);display:flex;align-items:center;justify-content:center}
.arrow svg{width:16px;height:16px}
.arrow.prev{left:0}.arrow.next{right:0}
.hero-copy{position:absolute;left:478px;top:78px;font-family:"Crimson Text",Georgia,serif;color:#222}
.hero-title{font-size:50px;letter-spacing:3px;line-height:1}
.hero-sub{font-size:29px;margin-left:20px;letter-spacing:1px;line-height:1.2}
.hero-text{margin-top:22px;font-style:italic;font-weight:700;font-size:24px;line-height:1.2;width:390px}
.cards{position:absolute;left:19px;top:493px;display:flex;gap:19px}
.card{width:286px;height:226px;background:#fff;padding:26px 14px 0 14px;box-shadow:0 0 6px rgba(0,0,0,.12)}
.card-title{font-size:24px;font-weight:400;color:var(--ink);white-space:nowrap}
.card-title span{color:var(--green)}
.card-text{margin-top:22px;font-size:11.5px;line-height:1.5;color:var(--muted)}
.more{display:inline-block;margin-top:30px;background:var(--purple);color:#fff;font-size:12px;padding:6px 16px;text-decoration:none}
.footer{position:absolute;left:0;top:772px;width:922px;height:54px;background:linear-gradient(var(--green-light),var(--green) 30%,var(--green-dark))}
.footer-text{position:absolute;left:24px;top:22px;color:#fff;font-size:11px;white-space:nowrap}
.footer-badge{position:absolute;left:411px;top:-24px;width:100px;height:100px;border-radius:50%;background:radial-gradient(#fff 55%,#dcdcdc);box-shadow:0 2px 6px rgba(0,0,0,.25)}
.social{position:absolute;right:46px;top:12px;display:flex;gap:6px}
.social i{width:28px;height:28px;display:block;border-radius:3px}
.social .s1{background:#3b5a98}.social .s2{background:#3fa9dd}.social .s3{background:#c41200}
</style>
</head>
<body>
<div class="page">
  <header>
    <div class="brand"><span class="brand-dot"></span><span class="brand-name">Skin Harbor Care</span></div>
    <div class="phone">
      <svg viewBox="0 0 24 24"><rect width="24" height="24" rx="4" fill="#4f9a1f"/><path d="M8 5l2 3-1.5 1.5a9 9 0 0 0 6 6L16 14l3 2-1 3c-6 0-12-6-12-12z" fill="#fff"/></svg>
      +555 - 014 -2368
    </div>
    <nav class="nav">
      <a class="active" href="#">Home</a><a href="#">About Us</a><a href="#">Location &amp; Hours</a><a href="#">Patient Resources</a><a href="#">Contact Us</a>
    </nav>
    <div class="nav-rule"></div>
  </header>

  <section class="hero">
    <div class="hero-photo" role="img" aria-label="Photo of a woman with clear skin holding a pink lily, against soft white flowers and green foliage"></div>
    <span class="arrow prev"><svg viewBox="0 0 16 16"><path d="M11 2L5 8l6 6" stroke="#777" stroke-width="3" fill="none"/></svg></span>
    <span class="arrow next"><svg viewBox="0 0 16 16"><path d="M5 2l6 6-6 6" stroke="#777" stroke-width="3" fill="none"/></svg></span>
    <div class="hero-copy">
      <div class="hero-title">We understand</div>
      <div class="hero-sub">how important your skin is...</div>
      <p class="hero-text">We are a specialized dermatology practice offering you the latest and most advanced procedures to treat your skin condition</p>
    </div>
  </section>

  <section class="cards">
    <article class="card">
      <h2 class="card-title">Why <span>Choose Us?</span></h2>
      <p class="card-text">Lorem ipsum dolor sit amet, consectetuer adipiscing elit, sed diam nonummy nibh euismod tincidunt ut laoreet dolore magna aliquam erat volutpat. Ut wisi enim ad minim veniam, quis nostrud exerci tation</p>
      <a class="more" href="#">Read More +</a>
    </article>
    <article class="card">
      <h2 class="card-title">Clinical <span>Skin Care</span></h2>
      <p class="card-text">Lorem ipsum dolor sit amet, consectetuer adipiscing elit, sed diam nonummy nibh euismod tincidunt ut laoreet dolore magna aliquam erat volutpat. Ut wisi enim ad minim veniam, quis nostrud exerci tation</p>
      <a class="more" href="#">Read More +</a>
    </article>
    <article class="card">
      <h2 class="card-title">Cosmetic <span>Skin Care</span></h2>
      <p class="card-text">Lorem ipsum dolor sit amet, consectetuer adipiscing elit, sed diam nonummy nibh euismod tincidunt ut laoreet dolore magna aliquam erat volutpat. Ut wisi enim ad minim veniam, quis nostrud exerci tation</p>
      <a class="more" href="#">Read More +</a>
    </article>
  </section>

  <footer class="footer">
    <div class="footer-text">©2013 Skin Harbor Care &nbsp;|&nbsp; Terms &nbsp;|&nbsp; Privacy</div>
    <div class="footer-badge"></div>
    <div class="social"><i class="s1"></i><i class="s2"></i><i class="s3"></i></div>
  </footer>
</div>
</body>
</html>
```